Business Card Design for new social media business

I am looking for a new professional business card design for an exciting new company which is based on providing members with experiences of others to benefit their choice of places to visit for restaurants, bars, clubs, national monument, tourist sights, hotels and so forth.
Updates

Please submit designs as I will choose to commit the funds depending on designs.

Target Market(s)

Business Managers as well as directors alongside owners

Industry/Entity Type

Business

Requirements
Must have
• Logo design and symbols
Nice to have
• Logo / Symbol on the back of the business card and possibly the logo as if embedded/embossed on the business card.

```html
<!DOCTYPE html>
<html lang="en">
<head>
<meta charset="utf-8">
<title>Roamquill Business Card</title>
<link rel="stylesheet" href="https://fonts.googleapis.com/css2?family=Open+Sans:wght@400;600;700;800&display=swap">
<style>
  :root {
    --page: #e4e4e6;
    --card: #f3f3f3;
    --brand: #3b2fa6;
    --accent: #e8561f;
    --blue: #1f4e96;
    --blue-line: #2457a8;
    --ink: #1b1b1b;
    --band: #1a1a1a;
    --muted: #555;
    --white: #ffffff;
  }
  * { margin: 0; padding: 0; box-sizing: border-box; }
  html, body { width: 1200px; height: 1152px; overflow: hidden; }
  body {
    background: var(--page);
    font-family: "Open Sans", Arial, sans-serif;
    position: relative;
  }
  .card {
    position: absolute;
    left: 130px;
    width: 940px;
    height: 530px;
    background: var(--card);
    box-shadow: 0 6px 18px rgba(0,0,0,.18);
    overflow: hidden;
  }
  .card--front { top: 34px; }
  .card--back { top: 588px; }

  .card__stripe {
    position: absolute;
    left: 0; right: 0; bottom: 0;
    height: 80px;
    background: var(--band);
    border-top: 5px solid var(--blue-line);
  }
  .card__stripe::before {
    content: "";
    position: absolute;
    left: 0; right: 0; top: 0;
    height: 4px;
    background: var(--white);
  }

  .brand { position: absolute; display: flex; flex-direction: column; }
  .brand__row { display: flex; align-items: center; gap: 22px; }
  .brand__mark {
    border-radius: 50%;
    background: var(--accent);
    flex: none;
  }
  .brand__name {
    font-weight: 700;
    color: var(--brand);
    letter-spacing: -2px;
    line-height: 1;
    white-space: nowrap;
  }
  .brand__tagline {
    color: var(--muted);
    font-weight: 400;
    white-space: nowrap;
  }

  .card--front .brand { left: 170px; top: 170px; }
  .card--front .brand__mark { width: 90px; height: 90px; }
  .card--front .brand__name { font-size: 108px; }
  .card--front .brand__tagline { font-size: 22px; letter-spacing: 9px; margin: 12px 0 0 130px; }

  .card--back .brand { left: 40px; top: 205px; }
  .card--back .brand__row { gap: 12px; }
  .card--back .brand__mark { width: 50px; height: 50px; }
  .card--back .brand__name { font-size: 64px; }
  .card--back .brand__tagline { font-size: 17px; letter-spacing: 6px; margin: 10px 0 0 30px; }

  .person { position: absolute; left: 470px; top: 40px; display: flex; align-items: baseline; gap: 10px; }
  .person__name { font-size: 32px; font-weight: 700; color: var(--ink); letter-spacing: .5px; }
  .person__role { font-size: 19px; font-weight: 600; color: var(--ink); }

  .contact { position: absolute; left: 470px; top: 92px; right: 0; list-style: none; }
  .contact__item {
    display: flex;
    align-items: center;
    height: 44px;
    margin-bottom: 8px;
    background: var(--blue);
    color: var(--white);
    font-size: 17px;
    font-weight: 400;
    padding-left: 18px;
    gap: 20px;
    white-space: nowrap;
  }
  .contact__arrow { width: 10px; height: 14px; flex: none; }
</style>
</head>
<body>

<section class="card card--front" aria-label="Card front">
  <div class="brand">
    <div class="brand__row">
      <span class="brand__mark"></span>
      <span class="brand__name">Roamquill</span>
    </div>
    <span class="brand__tagline">your business tagline</span>
  </div>
  <div class="card__stripe"></div>
</section>

<section class="card card--back" aria-label="Card back">
  <div class="brand">
    <div class="brand__row">
      <span class="brand__mark"></span>
      <span class="brand__name">Roamquill</span>
    </div>
    <span class="brand__tagline">your business tagline</span>
  </div>

  <div class="person">
    <span class="person__name">MIRA CASTELL</span>
    <span class="person__role">Work Manager</span>
  </div>

  <ul class="contact">
    <li class="contact__item"><svg class="contact__arrow" viewBox="0 0 10 14"><path d="M0 0L10 7L0 14Z" fill="#fff"/></svg>Address: 48 Harrow Lane, Westbrook NY 10234</li>
    <li class="contact__item"><svg class="contact__arrow" viewBox="0 0 10 14"><path d="M0 0L10 7L0 14Z" fill="#fff"/></svg>Tel Number: +1 555 0142 7788</li>
    <li class="contact__item"><svg class="contact__arrow" viewBox="0 0 10 14"><path d="M0 0L10 7L0 14Z" fill="#fff"/></svg>www.roamquill.example</li>
    <li class="contact__item"><svg class="contact__arrow" viewBox="0 0 10 14"><path d="M0 0L10 7L0 14Z" fill="#fff"/></svg>Fax Number: +1 555 0142 7788</li>
    <li class="contact__item"><svg class="contact__arrow" viewBox="0 0 10 14"><path d="M0 0L10 7L0 14Z" fill="#fff"/></svg>Email: hello@roamquill.example</li>
  </ul>

  <div class="card__stripe"></div>
</section>

</body>
</html>
```